Health Supplement Series for 60 tablets of pure Tamrel Vine Kernel powder

We need a packaging design theme for a health supplement for international consumers. Our initial product is called 'Tamrel Vine Kernel'. It is for general health and is particularly effective for diabetic symptoms.
We would like to see designs that are clean and fresh.
It should give the impression of professional, premium pharmaceutical grade products.
Our company logo is attached below.

Target Market(s)

International

Industry/Entity Type

Health And Wellness

Font styles to use
Serif
Sans Serif

Requirements
Must have
• Bottle and box packaging required.
• 1st product is bottle of 60 tablets of 0.5gm each.
Should not have
• Seals and other "must buy" "guaranteed" etc

```html
<!DOCTYPE html>
<html lang="en">
<head>
<meta charset="UTF-8">
<title>Natural Tamrel Vine Kernel – Bottle Label</title>
<link href="https://fonts.googleapis.com/css2?family=Oswald:wght@300;400;700&family=Montserrat:wght@600&display=swap" rel="stylesheet">
<style>
  :root{
    --page-bg:#e4e3e3;
    --label-pink:#f6e8e6;
    --label-pink-deep:#efdcda;
    --label-cream:#f8efe8;
    --brand-green:#3f9a1f;
    --tab-green:#2f6b2a;
    --tab-dark:#1d3a1c;
    --ink:#2a2a2a;
    --ink-soft:#3a3a3a;
    --seed-brown:#7a4a2c;
    --seed-light:#b58460;
    --badge-bg:#262626;
    --badge-text:#f2f2f2;
  }
  *{margin:0;padding:0;box-sizing:border-box;}
  html,body{width:1189px;height:1200px;overflow:hidden;}
  body{background:var(--page-bg);position:relative;font-family:'Oswald',sans-serif;}

  .label{
    position:absolute;left:214px;top:105px;width:760px;height:990px;
    background:
      radial-gradient(ellipse at 25% 30%, var(--label-cream) 0%, transparent 55%),
      radial-gradient(ellipse at 80% 70%, var(--label-pink-deep) 0%, transparent 60%),
      linear-gradient(160deg, var(--label-pink) 0%, var(--label-cream) 50%, var(--label-pink) 100%);
    box-shadow:0 6px 24px rgba(0,0,0,.12);
  }
  .label__marble{position:absolute;inset:0;}

  .label__tab{
    position:absolute;left:333px;top:0;width:94px;height:125px;
    background:linear-gradient(135deg,var(--tab-green) 0%,var(--tab-dark) 45%,var(--tab-green) 100%);
  }

  .brand{
    position:absolute;top:225px;left:0;right:0;
    display:flex;justify-content:center;align-items:center;gap:12px;
  }
  .brand__mark{width:40px;height:40px;background:var(--brand-green);}
  .brand__name{
    font-family:'Montserrat',sans-serif;font-weight:600;color:var(--brand-green);
    font-size:22px;line-height:1.05;letter-spacing:1px;text-transform:uppercase;
  }

  .product-title{
    position:absolute;top:325px;left:0;right:0;text-align:center;
    font-family:'Oswald',sans-serif;font-weight:700;text-transform:uppercase;
    line-height:1.02;letter-spacing:-1px;
  }
  .product-title__top{display:block;font-size:108px;color:var(--ink);}
  .product-title__bottom{display:block;font-size:92px;color:var(--ink-soft);}

  .seed-photo{
    position:absolute;left:315px;top:570px;width:130px;height:100px;border-radius:50%;
    background:radial-gradient(ellipse at 45% 45%, var(--seed-light) 0%, var(--seed-brown) 60%, transparent 72%);
  }

  .tagline{position:absolute;left:180px;top:560px;width:400px;height:220px;}
  .tagline text{font-family:'Oswald',sans-serif;font-weight:400;font-size:30px;fill:var(--ink);letter-spacing:1px;}

  .count-badge{
    position:absolute;top:840px;left:50%;transform:translateX(-50%);
    background:var(--badge-bg);color:var(--badge-text);
    font-family:'Oswald',sans-serif;font-weight:300;font-size:32px;
    padding:4px 14px;border:2px solid #555;
  }
</style>
</head>
<body>
  <div class="label">
    <svg class="label__marble" viewBox="0 0 760 990" preserveAspectRatio="none" aria-hidden="true">
      <path d="M0 140 C180 90 300 260 520 200 S760 120 760 160" fill="none" stroke="#ffffff" stroke-opacity=".45" stroke-width="18"/>
      <path d="M0 780 C200 700 380 880 560 800 S760 720 760 760" fill="none" stroke="#ecd4d2" stroke-opacity=".6" stroke-width="22"/>
    </svg>

    <div class="label__tab" role="img" aria-label="Green textured accent band"></div>

    <div class="brand">
      <span class="brand__mark"></span>
      <span class="brand__name">Corvane<br>Biotech Limited</span>
    </div>

    <h1 class="product-title">
      <span class="product-title__top">Natural Tamrel</span>
      <span class="product-title__bottom">Vine Kernel</span>
    </h1>

    <div class="seed-photo" role="img" aria-label="Photo of cracked vine kernel seeds"></div>

    <svg class="tagline" viewBox="0 0 400 220">
      <defs>
        <path id="tagline-arc" d="M20 40 A180 150 0 0 0 380 40"/>
      </defs>
      <text><textPath href="#tagline-arc" startOffset="50%" text-anchor="middle">• VINE KERNEL TABLETS •</textPath></text>
    </svg>

    <div class="count-badge">60 tablets</div>
  </div>
</body>
</html>
```